IT support company needs Banner Ad for the top of their quote layout template

We need a banner Ad for the top of our for quote layout template so it is sent out on all our quotes

The banner size must be 827 x 100 pixels - anything larger than 60 KB can cause upload time issues

We have attached our logo and examples of the quote page to see how it looks in the context of the whole page.

Essential elements of the banner
- Must have our logo but this can be changed to be different colours if it makes the design work better i.e. Tidal Grove could be all in white

Colours
- Can use all of our standard colours - Orange, Black, Grey and White

Images
- As a premium IT support company we deal with people and technology so would like to see both of these Incorporated into the banner i.e. people using technology These images could be watermarked or one colour effect.

Look and Feel
- Professional, friendly, people, technology, premium

Target Market
Small business owners and managers

Industry/Entity Type

It Company

```html
<!DOCTYPE html>
<html lang="nl">
<head>
<meta charset="utf-8">
<title>Offerte DJ-000280</title>
<link rel="stylesheet" href="https://fonts.googleapis.com/css2?family=Carlito:wght@400;700&display=swap">
<style>
  :root {
    --ink: #111111;
    --accent-blue: #1a73c4;
    --rule-blue: #1f7fd0;
    --header-light: #e6f2fc;
    --header-mid: #b9dcf6;
    --row-alt: #f3f3f3;
    --brand-orange: #f07c12;
    --banner-light: #f6ebdd;
    --banner-mid: #d9b48d;
    --banner-dark: #8c6a4c;
    --photo-grey: #8a8a8a;
    --footer-light: #d9eefb;
    --footer-mid: #4fb4ec;
    --page: #ffffff;
  }
  * { margin: 0; padding: 0; box-sizing: border-box; }
  html, body { width: 888px; height: 1200px; overflow: hidden; background: var(--page); }
  body { font-family: "Carlito", "Calibri", Arial, sans-serif; color: var(--ink); }
  .page { width: 827px; height: 1118px; position: relative; transform: scale(1.0738); transform-origin: 0 0; }
  .abs { position: absolute; }

  .banner { left: 0; top: 0; width: 827px; height: 102px;
    background: linear-gradient(90deg, var(--banner-dark) 0%, var(--banner-mid) 18%, var(--banner-light) 45%, var(--banner-mid) 62%, var(--banner-light) 80%, #fbf6ef 100%); }
  .banner-rule { left: 0; top: 102px; width: 827px; height: 6px;
    background: linear-gradient(90deg, #5bb6ea, var(--rule-blue)); }
  .brand { left: 540px; top: 32px; font-size: 34px; font-weight: 700; color: var(--brand-orange); letter-spacing: 1px; }

  .doc-title { left: 26px; top: 141px; font-size: 21px; }
  .portrait { left: 26px; top: 180px; width: 98px; height: 130px;
    background: linear-gradient(180deg, #b5b5b5, var(--photo-grey) 60%, #3d3d3d); }
  .party { top: 178px; font-size: 13px; line-height: 17px; }
  .party h3 { font-weight: 400; color: var(--accent-blue); font-size: 16.5px; margin-bottom: 6px; }
  .party .bold { font-weight: 700; margin-bottom: 3px; }
  .party p { margin-bottom: 0; }
  .gap { height: 17px; }
  .section-rule { left: 26px; top: 322px; width: 774px; height: 3px; background: var(--rule-blue); }

  .section-title { left: 26px; font-size: 18px; }
  .table { left: 26px; width: 774px; border: 1px solid var(--ink); font-size: 13px; }
  .row { display: flex; height: 26px; align-items: center; }
  .row.head { height: 24px; background: linear-gradient(90deg, var(--header-mid), var(--header-light) 50%, var(--header-mid)); }
  .row.alt { background: var(--row-alt); }
  .cell { padding: 0 6px; height: 100%; display: flex; align-items: center; }
  .desc { flex: 1; }
  .num { justify-content: flex-end; border-left: 1px solid var(--ink); }
  .w108 { width: 108px; }
  .totals { right: 32px; font-size: 13px; line-height: 25px; text-align: right; }
  .totals .line { display: flex; justify-content: flex-end; }
  .totals .label { color: var(--accent-blue); }
  .totals .value { width: 108px; font-weight: 700; }

  .terms { left: 26px; top: 924px; font-size: 12.5px; }
  .sign-line { top: 996px; height: 1px; background: var(--ink); }
  .sign-label { top: 998px; font-size: 13px; }

  .footer { left: 0; top: 1073px; width: 827px; height: 45px;
    background: linear-gradient(90deg, var(--footer-light), var(--footer-mid) 55%, var(--footer-light));
    border-top: 5px solid var(--rule-blue); font-size: 13px; }
  .footer span { position: absolute; top: 13px; }
</style>
</head>
<body>
<div class="page">
  <div class="abs banner" role="img" aria-label="Warm sepia montage of business people working beside large technology gears"></div>
  <div class="abs brand">TIDAL GROVE</div>
  <div class="abs banner-rule"></div>

  <h1 class="abs doc-title" style="font-weight:400">Standard MSP&nbsp; #2</h1>
  <div class="abs portrait" role="img" aria-label="Portrait photo of the quote author"></div>

  <div class="abs party" style="left:135px">
    <h3>Opgesteld door:</h3>
    <p class="bold">Noah Brennan Ltd</p>
    <p>Noah Brennan</p>
    <div class="gap"></div>
    <p>Fax</p>
    <p>noah.brennan@quotewell.com</p>
  </div>
  <div class="abs party" style="left:360px">
    <h3>Opgesteld voor:</h3>
    <p class="bold">Copper Ridge</p>
    <p>2218 Larkin Ave.</p>
    <p>Dayton,&nbsp; 48210</p>
    <p>Rachel Odell</p>
    <p>paul.lister@bluefern.co.uk</p>
  </div>
  <div class="abs party" style="left:627px">
    <h3>Gegevens Offerte:</h3>
    <p class="bold">Offerte #: DJ-000280</p>
    <p>Versie: 1</p>
    <p>Leverdatum: 14/11/2017</p>
    <p>Vervaldatum: 31/12/2017</p>
  </div>
  <div class="abs section-rule"></div>

  <h2 class="abs section-title" style="top:341px;font-weight:400">Overzicht Offerte</h2>
  <div class="abs table" style="top:370px">
    <div class="row head"><div class="cell desc">Beschrijving</div><div class="cell num w108" style="border-left-color:transparent">Bedrag</div></div>
    <div class="row"><div class="cell desc">Initial Investment</div><div class="cell num w108">$800.00</div></div>
  </div>
  <div class="abs totals" style="top:424px">
    <div class="line"><span class="label">Subtotaal:</span><span class="value">$800.00</span></div>
    <div class="line"><span class="label">VAT:</span><span class="value">$160.00</span></div>
    <div class="line"><span class="label">Totaal:</span><span class="value">$960.00</span></div>
  </div>

  <h2 class="abs section-title" style="top:518px;font-weight:400">Overzicht Terugkerende Kosten</h2>
  <div class="abs table" style="top:546px">
    <div class="row head"><div class="cell desc">Beschrijving</div><div class="cell num w108" style="border-left-color:transparent">Bedrag</div></div>
    <div class="row"><div class="cell desc">Monitoring</div><div class="cell num w108">$375.00</div></div>
    <div class="row alt"><div class="cell desc">Support</div><div class="cell num w108">$65.00</div></div>
    <div class="row"><div class="cell desc">Fixed Hours</div><div class="cell num w108">$850.00</div></div>
  </div>
  <div class="abs totals" style="top:652px">
    <div class="line"><span class="label">Terugkerende totaal:</span><span class="value">$1,290.00</span></div>
  </div>

  <h2 class="abs section-title" style="top:696px;font-weight:400">*Optionele kosten</h2>
  <div class="abs table" style="top:724px">
    <div class="row head"><div class="cell desc">Beschrijving</div><div class="cell num w108">Recurring</div><div class="cell num w108">One-Time</div></div>
    <div class="row"><div class="cell desc">Monitoring</div><div class="cell num w108">$790.00</div><div class="cell num w108">$0.00</div></div>
    <div class="row alt"><div class="cell desc">Support</div><div class="cell num w108">$185.00</div><div class="cell num w108">$0.00</div></div>
    <div class="row"><div class="cell desc">Fixed Hours</div><div class="cell num w108">$695.00</div><div class="cell num w108">$0.00</div></div>
    <div class="row alt"><div class="cell desc">Add-on Services</div><div class="cell num w108">$850.00</div><div class="cell num w108">$0.00</div></div>
  </div>
  <div class="abs totals" style="top:856px">
    <div class="line"><span class="label">Optionele terugkerend bedrag:</span><span class="value">$2,520.00</span></div>
    <div class="line"><span class="label">Optionele ongeplande Subtotaal:</span><span class="value">$.00</span></div>
  </div>

  <p class="abs terms">Taxes, shipping, handling and other fees may apply.&nbsp; We reserve the right to cancel orders arising from pricing or other errors.</p>

  <div class="abs sign-line" style="left:26px;width:463px"></div>
  <div class="abs sign-line" style="left:519px;width:181px"></div>
  <span class="abs sign-label" style="left:26px">Handtekening</span>
  <span class="abs sign-label" style="left:520px">Datum</span>

  <div class="abs footer">
    <span style="left:26px">Offerte #DJ-000280 v1</span>
    <span style="right:28px">Pagina 6 Van 7</span>
  </div>
</div>
</body>
</html>
```